Our Work

I would like to Upload Pictures and make a flyer showing some of the services we offer. I have attached a sample flyer layout and pictures I would like to use with the services labeled.

```html
<!DOCTYPE html>
<html lang="en">
<head>
<meta charset="utf-8">
<title>Kestrel Contracting Flyer</title>
<link href="https://fonts.googleapis.com/css2?family=Montserrat:wght@400;500;600;700;800;900&display=swap" rel="stylesheet">
<style>
  :root{
    --navy:#232f8f;
    --lavender:#a9a8d8;
    --yellow:#f7c230;
    --yellow-bright:#f8d63a;
    --purple:#4a3f9e;
    --ink:#2b2b2b;
    --paper:#ffffff;
    --header-bg:#f1f1f3;
  }
  *{margin:0;padding:0;box-sizing:border-box}
  html,body{width:877px;height:1200px;overflow:hidden;background:var(--paper)}
  body{font-family:'Montserrat',sans-serif;color:var(--ink)}
  .flyer{position:relative;width:877px;height:1200px;overflow:hidden;background:var(--paper)}

  .header{position:absolute;left:0;top:0;width:877px;height:205px;background:var(--header-bg)}
  .floorplan{position:absolute;left:470px;top:0;width:407px;height:205px;
    background:linear-gradient(135deg,#f1f1f3 0%,#e4e4e8 55%,#ededf0 100%)}
  .brand{position:absolute;left:60px;top:39px;width:320px;height:126px;background:#fff;
    display:flex;flex-direction:column;justify-content:center;padding-left:16px}
  .brand-name{font-weight:700;color:var(--navy);font-size:40px;line-height:1.05;letter-spacing:1px;text-transform:uppercase}
  .brand-name span{display:block;font-size:24px;letter-spacing:4px}
  .header-url{position:absolute;left:595px;top:145px;font-weight:700;font-size:16px;color:var(--navy)}

  .hero{position:absolute;left:0;top:205px;width:877px;height:404px;
    background:linear-gradient(100deg,#6d6d6d 0%,#3a3a3a 40%,#4f4f4f 70%,#2e2e2e 100%)}
  .hero-title{position:absolute;left:63px;top:300px;font-weight:900;color:#fff;font-size:112px;line-height:1;letter-spacing:-2px}
  .hero-sub{position:absolute;left:61px;top:418px;font-weight:800;color:var(--yellow);font-size:60px;line-height:1;letter-spacing:-1px}
  .hero-rule{position:absolute;left:60px;top:488px;width:725px;height:3px;background:var(--yellow)}

  .gallery{position:absolute;top:538px;left:58px;display:flex;gap:6px}
  .frame{width:252px;height:219px;border:3px solid var(--yellow);padding:9px;background:#fff}
  .photo{width:100%;height:100%}
  .photo-siding{background:linear-gradient(160deg,#c9c6c2 0%,#8a7258 50%,#b7b9bd 100%)}
  .photo-house{background:linear-gradient(180deg,#3f63c6 0%,#d9d9dc 45%,#a4583b 75%,#4f7a3a 100%)}
  .photo-door{background:linear-gradient(180deg,#6b4b37 0%,#d6d4d0 40%,#6f7b5b 75%,#4c5a8a 100%)}

  .services-title{position:absolute;left:60px;top:786px;font-weight:900;color:var(--lavender);font-size:45px;letter-spacing:-1px;white-space:nowrap}
  .service-list{position:absolute;top:844px;list-style:none;font-size:17px;line-height:20.6px;font-weight:500;color:#333}
  .service-list li{position:relative;padding-left:19px;white-space:nowrap}
  .service-list li::before{content:"";position:absolute;left:1px;top:9px;width:4px;height:4px;border-radius:50%;background:#333}
  .col-1{left:64px}.col-2{left:372px}.col-3{left:600px}

  .footer{position:absolute;left:0;top:1026px;width:877px;height:174px;
    background:linear-gradient(90deg,var(--purple) 0%,#5a4ea6 35%,#b89a78 58%,var(--yellow-bright) 72%,var(--yellow-bright) 100%)}
  .perks{position:absolute;left:60px;top:44px;list-style:none;color:#fff;font-weight:700;font-size:17.5px;line-height:21px;text-transform:uppercase}
  .perks li{display:flex;align-items:center;gap:6px;white-space:nowrap}
  .perks li.cont{padding-left:28px}
  .perks svg{width:22px;height:18px;flex:none}
  .contact{position:absolute;left:515px;top:36px;color:#1f1f1f}
  .contact-site{font-weight:600;font-size:21px;line-height:26px}
  .contact-phone{font-weight:600;font-size:44px;line-height:48px;letter-spacing:-0.5px}
  .contact-mail{font-weight:600;font-size:21px;line-height:26px}
</style>
</head>
<body>
<div class="flyer">
  <header class="header">
    <div class="floorplan" role="img" aria-label="Faint architectural floor plan drawing"></div>
    <div class="brand">
      <div class="brand-name">Kestrel<span>Contracting</span></div>
    </div>
    <div class="header-url">www.Kestrelcontracting.com</div>
  </header>

  <section class="hero" role="img" aria-label="Black and white photo of painters on scaffolding in a tall interior stairwell"></section>
  <div class="hero-title">KESTREL</div>
  <div class="hero-sub">CONTRACTING</div>
  <div class="hero-rule"></div>

  <div class="gallery">
    <div class="frame"><div class="photo photo-siding" role="img" aria-label="Workers on ladders repairing exterior siding around windows"></div></div>
    <div class="frame"><div class="photo photo-house" role="img" aria-label="Brick townhouse with house wrap installed during siding work"></div></div>
    <div class="frame"><div class="photo photo-door" role="img" aria-label="Crew installing a sliding patio door under a deck"></div></div>
  </div>

  <h2 class="services-title">EXTERIOR &amp; INTERIOR PAINTING</h2>
  <ul class="service-list col-1">
    <li>General Carpentry</li>
    <li>Framing Repairs</li>
    <li>Siding/Gutters/Windows/Doors</li>
    <li>Concrete Walkways/Stoops</li>
    <li>Balcony/Deck Rehab</li>
    <li>Tuckpointing</li>
    <li>Sealants/Caulks</li>
  </ul>
  <ul class="service-list col-2">
    <li>Pressure Washing</li>
    <li>Specialty Coatings</li>
    <li>Drywall Install/Repair</li>
    <li>Plaster Repairs</li>
    <li>Wallpaper Removal</li>
    <li>Flooring/Tile/Carpet</li>
    <li>Harhwood/Vinyl</li>
  </ul>
  <ul class="service-list col-3">
    <li>Leak Investigations:</li>
    <li>Facades, Roofs,</li>
    <li>Interior Leaks</li>
    <li>EIFS/Stucco Repairs</li>
    <li>Plumbing Repairs</li>
    <li>Roofing Repairs</li>
    <li>Lead Safe Renovations</li>
  </ul>

  <footer class="footer">
    <ul class="perks">
      <li><svg viewBox="0 0 22 18"><path d="M2 9 L8 15 L20 2" fill="none" stroke="#fff" stroke-width="3" stroke-linecap="round" stroke-linejoin="round"/></svg>Quick Estimates</li>
      <li><svg viewBox="0 0 22 18"><path d="M2 9 L8 15 L20 2" fill="none" stroke="#fff" stroke-width="3" stroke-linecap="round" stroke-linejoin="round"/></svg>Yearly Maintenance Contracts</li>
      <li><svg viewBox="0 0 22 18"><path d="M2 9 L8 15 L20 2" fill="none" stroke="#fff" stroke-width="3" stroke-linecap="round" stroke-linejoin="round"/></svg>Fast Response to General Services</li>
      <li class="cont">Work Order Repairs, Guaranteed!!!</li>
    </ul>
    <div class="contact">
      <div class="contact-site">Kestrelcontracting.com</div>
      <div class="contact-phone">555.214.0377</div>
      <div class="contact-mail">info@kestrelcontracting.com</div>
    </div>
  </footer>
</div>
</body>
</html>
```